Collective strata website refresh brellowquay.net.au

Description:
This website is managed by the leadership of a group of buildings in Harlow Point. The area and the collective stratas are known as Brellow Quay. The current website is messy and very dated. For the new site, we'd like to focus on a clean, user friendly design. The majority of the content on this site will be text. Most pages will use a one-pager scrolling format.

Current Site:
The current site is brellowquay.net.au

This site is functionally very good, but has certain issues due to its age. We are generally quite happy with the functionality of the site, despite layout issues.

Users:

The users are those who currently live or are interested in living in Brellow quay. This group has a large demographic spread, notably including a large amount of older people. When designing remember people who may be less familiar with technology and the internet will make up many of the users of the site. 

Design:
This site should give a clean, professional and welcoming energy. It should be clean, simple and focused on efficiently displaying information to the user in an accessible and clear way.
As users typically come to the site looking for a specific piece of information or to use a service

We would like a navigation menu with the categories "Home, Services, Facilities, Stratas, About Us, Local Information, Contact”

For us to choose a winner, we would like you to design the home page, but the winner will be required to provide an example strata page (a page with some headings that link to articles below) and a standard page. They will also be required to provide all images used without charge.

If you are going to submit multiple designs or respond to feedback, please modify the menu and text layout between them. This is the most important part of the design, and multiple submissions with only minor aesthetic changes will be largely disregarded.

Requested:
Home Page

Winner to provide:
Strata Page
Standard page template

There are some photos you can use here:

https://www.trovik.net/temp/brellowquay.zip

It contains:
A couple of the boss's own photos
Some photos from a PDF pamphlet done by a large organisation you can use
The current logos

The boss has taken a couple of photos [sigh] so if there is a way in using them somewhere on the site please do. They are not critical to use.
You do not have to use any of the photos, and if you use others remember you must provide them free with the design.

Designs look the same

```html
<!DOCTYPE html>
<html lang="en">
<head>
<meta charset="utf-8">
<title>Brellow Quay – Community Living</title>
<link href="https://fonts.googleapis.com/css2?family=Crimson+Text:wght@400;600&family=Poppins:ital,wght@0,400;0,500;0,600;1,400&display=swap" rel="stylesheet">
<style>
:root{
  --blue:#1f5b9e;
  --blue-dark:#174a85;
  --blue-soft:#e7edf5;
  --blue-accent:#8eaedb;
  --ink:#151515;
  --text:#3a3a3a;
  --muted:#6a6a6a;
  --line:#d6dde7;
  --white:#ffffff;
  --star:#f5b417;
}
*{box-sizing:border-box;margin:0;padding:0}
html,body{width:1200px;height:4963px;overflow:hidden}
body{position:relative;background:var(--white);font-family:'Poppins',sans-serif;color:var(--text);font-size:12.5px;line-height:22px}
.section{position:absolute;left:0;width:1200px}
.abs{position:absolute}
.serif{font-family:'Crimson Text',serif;color:var(--ink);font-weight:400}
.eyebrow{font-size:11px;font-weight:600;letter-spacing:1.3px;color:var(--blue);text-transform:uppercase;line-height:14px}
.heading{font-family:'Crimson Text',serif;font-size:27px;line-height:36px;color:var(--ink);font-weight:400}
.btn{position:absolute;display:flex;align-items:center;justify-content:center;background:var(--blue);color:var(--white);font-size:12px;font-weight:500;border-radius:5px;height:34px;text-decoration:none}
.photo{position:absolute}
.center{text-align:center;left:0;width:1200px}

.site-header{top:0;height:70px;background:var(--white);box-shadow:0 1px 6px rgba(0,0,0,.06);z-index:3}
.brand{position:absolute;left:141px;top:9px;height:54px;width:96px;display:flex;align-items:center;justify-content:center;font-family:'Crimson Text',serif;font-size:17px;line-height:18px;color:var(--blue);text-align:center}
.nav{position:absolute;left:430px;top:25px;display:flex}
.nav a{font-size:12.5px;font-weight:500;color:var(--ink);text-decoration:none;margin-right:31px}
.nav a.active{color:var(--blue)}
.nav-contact{left:963px;top:17px;width:94px;height:36px}

.hero{top:70px;height:488px;overflow:hidden}
.hero-photo{position:absolute;left:0;top:0;width:1200px;height:488px;background:linear-gradient(90deg,#ffffff 0%,#ffffff 28%,rgba(255,255,255,.6) 45%,rgba(255,255,255,0) 62%),linear-gradient(180deg,#b9cde6 0%,#dfe7ef 35%,#b7bcc0 62%,#7f8f82 78%,#5d7892 88%,#dfe6ec 100%)}
.hero-welcome{left:141px;top:88px;font-size:32px;line-height:40px}
.hero-name{left:141px;top:133px;font-size:50px;line-height:58px;color:var(--blue)}
.hero-sub{left:141px;top:198px;font-size:46px;line-height:56px}
.hero-copy{left:141px;top:280px;width:420px;font-size:12px;line-height:22.5px;color:var(--ink)}
.hero .btn{left:141px;top:375px;width:115px}

.about{top:600px;height:500px}
.tick-list{list-style:none}
.tick-list li{display:flex;align-items:center;gap:10px;height:29px;font-size:12.5px;color:var(--ink)}

.services{top:1140px;height:540px}
.service-card{position:absolute;top:150px;width:290px}
.service-card .photo{position:relative;width:290px;height:207px}
.service-card h3{font-family:'Crimson Text',serif;font-weight:600;font-size:21px;color:var(--blue);text-align:center;margin-top:24px;line-height:28px}
.service-card p{font-size:11.5px;line-height:20px;text-align:center;margin-top:10px;color:var(--text)}
.service-card .btn{position:relative;margin:22px auto 0;width:112px}

.local{top:1739px;height:432px;background:var(--blue-soft);overflow:hidden}
.local-copy p{font-size:12.5px;line-height:22.5px;color:var(--ink);margin-bottom:14px}
.local-copy b{font-weight:600}

.whatson{top:2220px;height:470px}
.body-copy p{font-size:12.5px;line-height:22.5px;color:var(--text);margin-bottom:18px}

.facilities{top:2740px;height:360px}
.tile{position:absolute;top:122px;width:216px;height:220px;overflow:hidden}
.tile-label{position:absolute;left:15px;right:15px;bottom:14px;display:flex;justify-content:space-between;align-items:center;color:var(--white);font-size:12.5px;font-weight:500;letter-spacing:.4px}

.testimonials{top:3150px;height:460px}
.quote{left:553px;top:158px;width:430px;font-style:italic;font-size:11.5px;line-height:20px;color:var(--text)}
.person{left:553px;top:330px;font-size:17px;font-weight:600;color:var(--blue)}
.role{left:553px;top:357px;font-size:11px;color:var(--ink)}

.faq{top:3650px;height:380px}
.faq-num{font-size:34px;font-weight:600;color:#b3c6df;line-height:36px}
.faq-q{font-size:12.5px;font-weight:500;color:var(--ink);line-height:20px}
.faq-a{font-size:11.5px;line-height:20.5px;color:var(--text)}

.contact{top:4048px;height:532px;background:var(--blue-soft)}
.contact-item h4{font-size:16px;font-weight:500;color:var(--ink);line-height:22px}
.contact-item p{font-size:12.5px;line-height:20px;color:var(--ink);margin-top:4px}
.form-card{left:551px;top:180px;width:508px;height:294px;background:#d7e1ee;border-radius:10px}
.field{position:absolute;background:var(--white);border:1px solid var(--line);border-radius:5px;font-size:11px;color:#8a8a8a;padding:8px 12px;line-height:16px}

.site-footer{top:4580px;height:383px}
.footer-brand{left:141px;top:58px;width:206px;height:48px;display:flex;align-items:center;font-family:'Crimson Text',serif;font-size:25px;color:var(--blue);letter-spacing:.5px}
.footer-col h5{font-size:16px;font-weight:500;color:var(--blue);line-height:22px;margin-bottom:18px}
.footer-col a{display:block;font-size:12.5px;color:var(--ink);text-decoration:none;line-height:29px}
.footer-contact li{list-style:none;display:flex;gap:10px;font-size:12.5px;color:var(--ink);line-height:20px;margin-bottom:14px}
.divider{left:141px;width:916px;top:322px;height:1px;background:#cfd5dd}
.social{position:absolute;top:341px;width:23px;height:23px;border-radius:50%;background:var(--blue)}
</style>
</head>
<body>

<header class="section site-header">
  <div class="brand">Brellow<br>Quay</div>
  <nav class="nav">
    <a class="active" href="#">Home</a><a href="#">Services</a><a href="#">Facilities</a><a href="#">Stratas</a><a href="#">About Us</a><a href="#">Local Information</a>
  </nav>
  <a class="btn nav-contact" href="#">Contact</a>
</header>

<section class="section hero">
  <div class="hero-photo" role="img" aria-label="Harbourside skyline of apartment towers and a cable-stayed bridge under a blue sky"></div>
  <h2 class="abs serif hero-welcome">Welcome To</h2>
  <h1 class="abs serif hero-name">Brellow Quay</h1>
  <h2 class="abs serif hero-sub">Community Living</h2>
  <p class="abs hero-copy">Brellow Quay is a community of 2500 residents in more than 1000 apartments, terraces and townhouses on the site of the old Kestrel industrial complex.</p>
  <a class="btn" href="#">Learn More</a>
</section>

<section class="section about">
  <div class="photo" style="left:141px;top:41px;width:294px;height:378px;background:linear-gradient(180deg,#d98a2e 0%,#b86a22 30%,#6b7a3c 60%,#4f6e2c 100%)" role="img" aria-label="Residents relaxing on the harbour lawn at sunset with a boat passing"></div>
  <div class="photo" style="left:320px;top:290px;width:244px;height:175px;border:3px solid #fff;background:linear-gradient(180deg,#2d6db5 0%,#5d92cf 40%,#3c5a3e 75%,#1f3a5c 100%)" role="img" aria-label="Heritage house beside modern apartments on the waterfront"></div>
  <p class="abs eyebrow" style="left:616px;top:46px">About Us</p>
  <h2 class="abs heading" style="left:616px;top:70px;width:420px">Brellow Quay Community Living</h2>
  <p class="abs" style="left:616px;top:162px;width:444px;font-size:12.5px;line-height:22.5px;color:var(--text)">Brellow Quay is a community of 2500 residents in more than 1000 apartments, terraces and townhouses on the site of the old Kestrel industrial complex at the northern end of the Harlow Peninsula. In addition there are a number of commercial buildings housing several hundred workers.</p>
  <ul class="abs tick-list" style="left:616px;top:293px">
    <li><svg width="17" height="17" viewBox="0 0 17 17"><circle cx="8.5" cy="8.5" r="7.5" fill="none" stroke="#1f5b9e" stroke-width="1.4"/><path d="M5 8.8l2.4 2.3 4.6-4.8" fill="none" stroke="#1f5b9e" stroke-width="1.6"/></svg>Regular (and irregular) community activities</li>
    <li><svg width="17" height="17" viewBox="0 0 17 17"><circle cx="8.5" cy="8.5" r="7.5" fill="none" stroke="#1f5b9e" stroke-width="1.4"/><path d="M5 8.8l2.4 2.3 4.6-4.8" fill="none" stroke="#1f5b9e" stroke-width="1.6"/></svg>A map of Brellow Quay village</li>
    <li><svg width="17" height="17" viewBox="0 0 17 17"><circle cx="8.5" cy="8.5" r="7.5" fill="none" stroke="#1f5b9e" stroke-width="1.4"/><path d="M5 8.8l2.4 2.3 4.6-4.8" fill="none" stroke="#1f5b9e" stroke-width="1.6"/></svg>The latest copy of Brellow Quay What's On.</li>
  </ul>
  <a class="btn" href="#" style="left:616px;top:403px;width:112px">Read More</a>
</section>

<section class="section services">
  <p class="abs eyebrow" style="left:141px;top:22px">What We Do</p>
  <h2 class="abs heading" style="left:141px;top:46px">Our Service</h2>
  <div class="abs" style="left:494px;top:20px;width:3px;height:84px;background:var(--blue)"></div>
  <p class="abs" style="left:518px;top:18px;width:520px;font-size:12px;line-height:22.5px;color:var(--text)">The Community Association and some strata plans have contracts with Nelvo Cleaning to provide cleaning services. Others have contracted with TidyCove. There is a notebook in each mail room where you can leave notes for your building's cleaner.</p>

  <article class="service-card" style="left:141px">
    <div class="photo" role="img" aria-label="Orange brick apartment block under a blue sky" style="background:linear-gradient(180deg,#3d74c2 0%,#c0622e 40%,#9a4a22 75%,#5e7a3a 100%)"></div>
    <h3>Building Management</h3>
    <p>Each strata makes its own building management arrangements. Some have chosen to retain…</p>
    <a class="btn" href="#">Read More</a>
  </article>
  <article class="service-card" style="left:454px">
    <div class="photo" role="img" aria-label="Two residents walking along a leafy garden path" style="background:linear-gradient(180deg,#8aa52c 0%,#5b7c1d 45%,#3d5a17 100%)"></div>
    <h3>Security</h3>
    <p>Security officers are employed by Harbourline Guard Services (HGS), the company…</p>
    <a class="btn" href="#">Read More</a>
  </article>
  <article class="service-card" style="left:767px">
    <div class="photo" role="img" aria-label="Terraced apartments with balcony gardens" style="background:linear-gradient(180deg,#c9d4dd 0%,#b5b0a4 40%,#5d7a45 80%,#3e5a2f 100%)"></div>
    <h3>Strata Manager</h3>
    <p>Corvel Property Group is contracted by the Community Association to provide strata…</p>
    <a class="btn" href="#">Read More</a>
  </article>
</section>

<section class="section local">
  <div class="abs" style="left:0;top:0;width:1200px;height:432px;background:var(--blue-accent);clip-path:polygon(735px 0,1200px 0,1200px 432px,608px 432px)"></div>
  <div class="abs" style="left:0;top:0;width:1200px;height:432px;background:linear-gradient(180deg,#3a5f3c 0%,#c99a63 35%,#8c5b32 65%,#2a3d2b 100%);clip-path:polygon(762px 0,1200px 0,1200px 432px,636px 432px)" role="img" aria-label="Apartment tower lit at dusk among trees"></div>
  <p class="abs eyebrow" style="left:141px;top:60px">General Info</p>
  <h2 class="abs heading" style="left:141px;top:84px">Local Information</h2>
  <div class="abs local-copy" style="left:141px;top:138px;width:480px">
    <p><b>A regular bus service (389)</b> runs from Quayside Plaza around Tern Point, along Anvil Street to Vessel Street, and then through Fernmoor to Calder Junction and North Calder.</p>
    <p><b>A less regular bus service (501)</b> goes from the Seafood Hall up Tallow Street along Anvil Street to Depot Square.</p>
    <p><b>A ferry</b> goes from Harlow Bay (opposite Quayside Plaza next to the Harbour Museum) to Ferry Quay.</p>
  </div>
  <a class="btn" href="#" style="left:141px;top:355px;width:115px">Learn More</a>
</section>

<section class="section whatson">
  <div class="photo" style="left:141px;top:35px;width:294px;height:376px;background:linear-gradient(180deg,#4e6e22 0%,#88a43a 40%,#b89a55 70%,#5c7b2a 100%)" role="img" aria-label="Children playing in a leafy park"></div>
  <div class="photo" style="left:302px;top:274px;width:243px;height:177px;border:3px solid #fff;background:linear-gradient(180deg,#d9e2ea 0%,#cfc7b8 45%,#4f7b2c 80%,#3f6325 100%)" role="img" aria-label="Apartment towers behind a green lawn with residents"></div>
  <p class="abs eyebrow" style="left:616px;top:40px">What's On</p>
  <h2 class="abs heading" style="left:616px;top:64px">BQ What's On</h2>
  <div class="abs body-copy" style="left:616px;top:118px;width:444px">
    <p>Brellow Quay What's On is a monthly newsletter produced and distributed by and for residents of Brellow Quay and the wider Harlow Point community. It aims to keep you up-to-date with BQ and local activities. If you wish to contribute, email Dana before the 20th of the month. If you have an event to advertise, email Ruth.</p>
    <p>If you do not receive your copy of Brellow Quay What's On by the first week of the month, ring Ruth on 0400 118 362. Extra copies can be obtained from the Estate Management office in Carrow Street.Click here to download the current issue.</p>
  </div>
  <a class="btn" href="#" style="left:616px;top:365px;width:112px">Read More</a>
</section>

<section class="section facilities">
  <p class="abs eyebrow center" style="top:20px">Facilities</p>
  <h2 class="abs heading center" style="top:44px">The Community Association</h2>
  <div class="tile" style="left:141px">
    <div class="abs" style="inset:0;background:linear-gradient(180deg,#6e8a4d 0%,#a99b78 45%,#3e5330 100%)" role="img" aria-label="Aerial view of the tennis courts and gardens"></div>
    <div class="tile-label"><span>TENNIS COURTS</span><svg width="20" height="12" viewBox="0 0 20 12"><path d="M1 6h17M13 1l5 5-5 5" fill="none" stroke="#fff" stroke-width="1.5"/></svg></div>
  </div>
  <div class="tile" style="left:375px">
    <div class="abs" style="inset:0;background:linear-gradient(180deg,#1d2a3a 0%,#6e8fa3 35%,#9ec7cf 65%,#3b4e52 100%)" role="img" aria-label="Indoor glasshouse swimming pool"></div>
    <div class="tile-label"><span>GLASSHOUSE POOL</span><svg width="20" height="12" viewBox="0 0 20 12"><path d="M1 6h17M13 1l5 5-5 5" fill="none" stroke="#fff" stroke-width="1.5"/></svg></div>
  </div>
  <div class="tile" style="left:609px">
    <div class="abs" style="inset:0;background:linear-gradient(180deg,#8ea6c2 0%,#546d88 45%,#2c3a4a 100%)" role="img" aria-label="Residents exercising on treadmills in the gym"></div>
    <div class="tile-label"><span>GLASSHOUSE GYM</span><svg width="20" height="12" viewBox="0 0 20 12"><path d="M1 6h17M13 1l5 5-5 5" fill="none" stroke="#fff" stroke-width="1.5"/></svg></div>
  </div>
  <div class="tile" style="left:842px">
    <div class="abs" style="inset:0;background:linear-gradient(180deg,#9fb9d8 0%,#9a9a5a 40%,#c9c93a 60%,#4a5a30 100%)" role="img" aria-label="The Station building with green facade"></div>
    <div class="tile-label"><span>THE STATION</span><svg width="20" height="12" viewBox="0 0 20 12"><path d="M1 6h17M13 1l5 5-5 5" fill="none" stroke="#fff" stroke-width="1.5"/></svg></div>
  </div>
</section>

<section class="section testimonials">
  <p class="abs eyebrow center" style="top:22px">Testimonials</p>
  <h2 class="abs heading center" style="top:46px">Our Happy Customers</h2>
  <div class="photo" style="left:204px;top:124px;width:274px;height:280px;background:linear-gradient(180deg,#d8d8d8 0%,#9a9a9a 55%,#2e2e2e 100%)" role="img" aria-label="Black and white portrait of the reviewer in a suit"></div>
  <svg class="abs" style="left:553px;top:128px" width="82" height="15" viewBox="0 0 82 15">
    <g fill="#f5b417"><polygon points="7.5,0 9.3,5.2 15,5.4 10.5,8.8 12.1,14.2 7.5,11 2.9,14.2 4.5,8.8 0,5.4 5.7,5.2"/><polygon transform="translate(16.5 0)" points="7.5,0 9.3,5.2 15,5.4 10.5,8.8 12.1,14.2 7.5,11 2.9,14.2 4.5,8.8 0,5.4 5.7,5.2"/><polygon transform="translate(33 0)" points="7.5,0 9.3,5.2 15,5.4 10.5,8.8 12.1,14.2 7.5,11 2.9,14.2 4.5,8.8 0,5.4 5.7,5.2"/><polygon transform="translate(49.5 0)" points="7.5,0 9.3,5.2 15,5.4 10.5,8.8 12.1,14.2 7.5,11 2.9,14.2 4.5,8.8 0,5.4 5.7,5.2"/><polygon transform="translate(66 0)" points="7.5,0 9.3,5.2 15,5.4 10.5,8.8 12.1,14.2 7.5,11 2.9,14.2 4.5,8.8 0,5.4 5.7,5.2"/></g>
  </svg>
  <p class="abs quote">" The unique waterfront position, unparalleled access to Harlow Point's finest selection of restaurants, cafes, essential services, shopping and a variety of public transport connections to the city caters to a variety of buyer requirements. Having seen first-hand Brellow Quay residents buying multiple properties from us or continually upgrading their home is a true testament to the quality apartments we've crafted in a world-class community. "</p>
  <p class="abs person">-Simon Ardley</p>
  <p class="abs role">State Manager, East Region - Apartments Development</p>
  <svg class="abs" style="left:556px;top:398px" width="20" height="12" viewBox="0 0 20 12"><path d="M19 6H2M7 1L2 6l5 5" fill="none" stroke="#1f5b9e" stroke-width="1.5"/></svg>
  <svg class="abs" style="left:602px;top:390px" width="29" height="29" viewBox="0 0 29 29"><circle cx="14.5" cy="14.5" r="14.5" fill="#1f5b9e"/><path d="M8 14.5h12M16 10l4.5 4.5L16 19" fill="none" stroke="#fff" stroke-width="1.6"/></svg>
</section>

<section class="section faq">
  <p class="abs eyebrow center" style="top:15px">FAQ's</p>
  <h2 class="abs heading center" style="top:40px">Community Facilities</h2>

  <span class="abs faq-num" style="left:141px;top:124px">01</span>
  <p class="abs faq-q" style="left:189px;top:132px">What av equipment is available in the station?</p>
  <svg class="abs" style="left:548px;top:133px" width="19" height="19" viewBox="0 0 19 19"><circle cx="9.5" cy="9.5" r="9.5" fill="#1f5b9e"/><path d="M5.5 11.5l4-4 4 4" fill="none" stroke="#fff" stroke-width="1.6"/></svg>
  <p class="abs faq-a" style="left:189px;top:168px;width:385px">There is a large colour projector for DVD, HD TV and computers. Audio – radio and CD – is available via MP3 player. It is recommended that computer systems are trialled prior to the event as some older systems have been found to be incompatible.</p>

  <span class="abs faq-num" style="left:141px;top:268px">03</span>
  <p class="abs faq-q" style="left:196px;top:276px">I've heard there's a book exchange. where is it?</p>
  <svg class="abs" style="left:548px;top:277px" width="19" height="19" viewBox="0 0 19 19"><circle cx="9.5" cy="9.5" r="9.5" fill="#1f5b9e"/><path d="M5.5 7.5l4 4 4-4" fill="none" stroke="#fff" stroke-width="1.6"/></svg>

  <span class="abs faq-num" style="left:628px;top:130px">02</span>
  <p class="abs faq-q" style="left:682px;top:128px;width:310px">How do i find out about the history of brellow quay?</p>
  <svg class="abs" style="left:1039px;top:133px" width="19" height="19" viewBox="0 0 19 19"><circle cx="9.5" cy="9.5" r="9.5" fill="#1f5b9e"/><path d="M5.5 7.5l4 4 4-4" fill="none" stroke="#fff" stroke-width="1.6"/></svg>

  <span class="abs faq-num" style="left:624px;top:200px">04</span>
  <p class="abs faq-q" style="left:682px;top:204px">What community facility does harlow point have?</p>
  <svg class="abs" style="left:1039px;top:205px" width="19" height="19" viewBox="0 0 19 19"><circle cx="9.5" cy="9.5" r="9.5" fill="#1f5b9e"/><path d="M5.5 7.5l4 4 4-4" fill="none" stroke="#fff" stroke-width="1.6"/></svg>
</section>

<section class="section contact">
  <p class="abs eyebrow center" style="top:66px">Contact</p>
  <h2 class="abs heading center" style="top:92px">General Contacts</h2>

  <svg class="abs" style="left:141px;top:243px" width="26" height="28" viewBox="0 0 26 28"><path d="M13 2a7.5 7.5 0 0 0-7.5 7.5c0 5.5 7.5 13 7.5 13s7.5-7.5 7.5-13A7.5 7.5 0 0 0 13 2z" fill="none" stroke="#1f5b9e" stroke-width="2"/><circle cx="13" cy="9.5" r="2.8" fill="#1f5b9e"/><path d="M5 21c-3 1-3 4 8 4s11-3 8-4" fill="none" stroke="#1f5b9e" stroke-width="1.6"/></svg>
  <div class="abs contact-item" style="left:187px;top:239px">
    <h4>Address</h4>
    <p>Shop 4/12 Wharfside Road,<br>Harlow Point 2999</p>
  </div>
  <svg class="abs" style="left:143px;top:330px" width="24" height="24" viewBox="0 0 24 24"><path d="M6.6 10.8a15.2 15.2 0 0 0 6.6 6.6l2.2-2.2c.3-.3.7-.4 1-.2 1.1.4 2.3.6 3.6.6.6 0 1 .4 1 1V20c0 .6-.4 1-1 1A17 17 0 0 1 3 4c0-.6.4-1 1-1h3.5c.6 0 1 .4 1 1 0 1.3.2 2.5.6 3.6.1.3 0 .7-.2 1z" fill="#1f5b9e"/></svg>
  <div class="abs contact-item" style="left:187px;top:326px">
    <h4>Phone</h4>
    <p>02 9000 4821</p>
  </div>
  <svg class="abs" style="left:143px;top:405px" width="24" height="18" viewBox="0 0 24 18"><rect x="1" y="1" width="22" height="16" rx="1.5" fill="none" stroke="#1f5b9e" stroke-width="2"/><path d="M1.5 2l10.5 8 10.5-8" fill="none" stroke="#1f5b9e" stroke-width="2"/></svg>
  <div class="abs contact-item" style="left:187px;top:398px">
    <h4>Email us</h4>
    <p>info@brellowquay.net.au</p>
  </div>

  <form class="abs form-card">
    <div class="field" style="left:19px;top:21px;width:226px;height:35px">First name</div>
    <div class="field" style="left:260px;top:21px;width:226px;height:35px">Last name</div>
    <div class="field" style="left:19px;top:67px;width:226px;height:35px">Email</div>
    <div class="field" style="left:260px;top:67px;width:226px;height:35px">Phone</div>
    <div class="field" style="left:19px;top:113px;width:467px;height:102px">Message</div>
    <span class="btn" style="left:187px;top:242px;width:131px">Send Message</span>
  </form>
</section>

<footer class="section site-footer">
  <div class="abs footer-brand">BRELLOW QUAY</div>
  <p class="abs" style="left:141px;top:130px;width:240px;font-size:11px;line-height:20px;color:var(--ink)">Brellow Quay is a community of 2500 residents in more than 1000 apartments.</p>

  <div class="abs footer-col" style="left:455px;top:60px">
    <h5>Quick Links</h5>
    <a href="#">Home</a><a href="#">Services</a><a href="#">Facilities</a><a href="#">Stratas</a><a href="#">About Us</a><a href="#">Local Information</a>
  </div>
  <div class="abs footer-col" style="left:626px;top:60px">
    <h5>Support</h5>
    <a href="#">Privacy Policy</a><a href="#">Terms of Use</a><a href="#">Contact Webmaster</a><a href="#">Contact Us</a>
  </div>
  <div class="abs footer-col" style="left:817px;top:60px">
    <h5>Contact</h5>
    <ul class="footer-contact">
      <li><svg width="18" height="20" viewBox="0 0 26 28"><path d="M13 2a7.5 7.5 0 0 0-7.5 7.5c0 5.5 7.5 13 7.5 13s7.5-7.5 7.5-13A7.5 7.5 0 0 0 13 2z" fill="none" stroke="#1f5b9e" stroke-width="2.4"/><circle cx="13" cy="9.5" r="2.8" fill="#1f5b9e"/></svg><span>Shop 4/12 Wharfside<br>Road, Harlow Point 2999</span></li>
      <li style="margin-top:10px"><svg width="18" height="14" viewBox="0 0 24 18"><rect x="1" y="1" width="22" height="16" rx="1.5" fill="none" stroke="#1f5b9e" stroke-width="2"/><path d="M1.5 2l10.5 8 10.5-8" fill="none" stroke="#1f5b9e" stroke-width="2"/></svg><span>info@brellowquay.net.au</span></li>
      <li><svg width="18" height="18" viewBox="0 0 24 24"><path d="M6.6 10.8a15.2 15.2 0 0 0 6.6 6.6l2.2-2.2c.3-.3.7-.4 1-.2 1.1.4 2.3.6 3.6.6.6 0 1 .4 1 1V20c0 .6-.4 1-1 1A17 17 0 0 1 3 4c0-.6.4-1 1-1h3.5c.6 0 1 .4 1 1 0 1.3.2 2.5.6 3.6.1.3 0 .7-.2 1z" fill="#1f5b9e"/></svg><span>02 9000 4821</span></li>
    </ul>
  </div>

  <div class="abs divider"></div>
  <p class="abs" style="left:141px;top:344px;font-size:11px;color:var(--ink)">© 2023 Brellowquay. All Rights Reserved</p>
  <span class="social" style="left:926px" aria-label="Social link"></span>
  <span class="social" style="left:961px" aria-label="Social link"></span>
  <span class="social" style="left:996px" aria-label="Social link"></span>
  <span class="social" style="left:1032px" aria-label="Social link"></span>
</footer>

</body>
</html>
```